KEM Logistics - Banner 2.5' x 8' for 20+ locations

Need a banner designed that will pop. This banner will be displayed at over 20 of our transportation facilities. Goal is for the banner to grab the attention of employees, contractors and clients and help reinforce our mission and core values. Designed needs to include KEM Logo, our core values and mission statement. Red and Black are the main company colors and we need to stay within that theme and color pallet. Attached is a previous version that was too basic and boring. Willing to consider a design that excludes the mission statement.

```html
<!DOCTYPE html>
<html lang="en">
<head>
<meta charset="utf-8">
<title>KEM Logistics – Core Values Banner</title>
<link href="https://fonts.googleapis.com/css2?family=Montserrat:wght@500;600;700&family=Oswald:wght@500&display=swap" rel="stylesheet">
<style>
  :root{
    --bg:#c9c9c9;
    --ink:#2b2a29;
    --red:#d42027;
    --red-deep:#a9161c;
    --white:#ffffff;
    --text:#2e2e2e;
  }
  html,body{margin:0;padding:0;width:857px;height:1200px;overflow:hidden;background:var(--bg);}
  .canvas{position:relative;width:857px;height:1200px;overflow:hidden;}
  .banner{
    position:absolute;left:258px;top:56px;width:398px;height:1270px;
    transform:scale(0.857);transform-origin:0 0;overflow:hidden;
    font-family:'Montserrat',sans-serif;
  }
  .banner-shapes{position:absolute;inset:0;}
  .brand-name{
    position:absolute;left:184px;top:378px;width:190px;text-align:center;
    font-family:'Montserrat',sans-serif;font-weight:700;font-size:25px;line-height:1.05;
    color:var(--ink);letter-spacing:.5px;
  }
  .values-title{
    position:absolute;left:0;top:535px;width:398px;text-align:center;margin:0;
    font-family:'Oswald',sans-serif;font-weight:500;font-size:44px;color:var(--red);
    letter-spacing:.5px;
  }
  .values-list{position:absolute;left:0;top:0;margin:0;padding:0;list-style:none;}
  .value{
    position:absolute;left:94px;width:290px;
    font-weight:700;font-size:17px;line-height:22px;color:var(--text);
    text-transform:uppercase;transform:translateY(-50%);
  }
  .mission{
    position:absolute;left:10px;top:1090px;width:378px;margin:0;text-align:center;
    color:var(--white);font-size:21.5px;line-height:25px;font-weight:500;
  }
  .mission strong{font-weight:700;}
</style>
</head>
<body>
<div class="canvas">
  <div class="banner">
    <svg class="banner-shapes" viewBox="0 0 398 1270" width="398" height="1270" xmlns="http://www.w3.org/2000/svg">
      <defs>
        <linearGradient id="photoTone" x1="0" y1="0" x2="0" y2="1">
          <stop offset="0" stop-color="#7a5a3a"/>
          <stop offset=".55" stop-color="#a08468"/>
          <stop offset="1" stop-color="#c7c9cc"/>
        </linearGradient>
        <linearGradient id="redSweep" x1="0" y1="0" x2="1" y2="0">
          <stop offset="0" stop-color="var(--red-deep)"/>
          <stop offset="1" stop-color="var(--red)"/>
        </linearGradient>
        <clipPath id="photoClip"><circle cx="199" cy="205" r="172"/></clipPath>
      </defs>
      <rect class="backdrop" width="398" height="1270" fill="var(--ink)"/>
      <path class="top-red-curve" d="M0,220 Q30,350 200,385 L398,378 L398,395 L0,395 Z" fill="url(#redSweep)"/>
      <path class="body-panel" d="M0,368 Q140,400 398,372 L398,985 Q260,1060 130,1045 Q50,1030 0,965 Z" fill="var(--white)"/>
      <path class="bottom-red-curve" d="M130,1045 Q280,1055 398,985 L398,1068 Q250,1068 130,1045 Z" fill="url(#redSweep)"/>
      <circle class="photo-ring" cx="199" cy="205" r="180" fill="var(--white)"/>
      <g clip-path="url(#photoClip)">
        <rect role="img" aria-label="Photo of a warehouse aisle with a worker driving a yellow forklift between tall shelves of boxes" x="19" y="25" width="360" height="360" fill="url(#photoTone)"/>
      </g>
      <circle class="brand-badge" cx="279" cy="410" r="93" fill="var(--white)" stroke="var(--red)" stroke-width="6"/>

      <g class="value-icons" fill="var(--red)">
        <circle cx="49" cy="632" r="19"/>
        <circle cx="49" cy="695" r="19"/>
        <circle cx="49" cy="758" r="19"/>
        <circle cx="49" cy="820" r="19"/>
        <circle cx="49" cy="884" r="19"/>
        <circle cx="49" cy="945" r="19"/>
      </g>
      <g class="value-glyphs" fill="none" stroke="var(--white)" stroke-width="2.4" stroke-linecap="round" stroke-linejoin="round">
        <path d="M40,632 l6,6 l12,-12"/>
        <path d="M41,703 v-5 M46,703 v-8 M51,703 v-11 M56,703 v-14 M39,704 h20"/>
        <path d="M49,748 l10,17 h-20 Z M49,756 v4"/>
        <path d="M49,809 l3,7 h7 l-6,5 l2,7 l-6,-4 l-6,4 l2,-7 l-6,-5 h7 Z"/>
        <path d="M49,873 l9,4 v6 q0,8 -9,12 q-9,-4 -9,-12 v-6 Z"/>
        <circle cx="49" cy="945" r="9"/>
        <path d="M45,948 q4,4 8,0"/>
      </g>
    </svg>

    <div class="brand-name">KEM<br>LOGISTICS</div>

    <h2 class="values-title">CORE VALUES</h2>
    <ul class="values-list">
      <li class="value" style="top:632px">Do the right things for the right reasons</li>
      <li class="value" style="top:695px">Pursue growth and development</li>
      <li class="value" style="top:758px">Build a positive team atmosphere</li>
      <li class="value" style="top:820px">Deliver wow through service</li>
      <li class="value" style="top:884px">Do everything safely</li>
      <li class="value" style="top:945px">Have fun</li>
    </ul>

    <p class="mission"><strong>Provide the best customer experience while creating an environment of</strong><br>growth and opportunity for our customers, employees, and service providers.</p>
  </div>
</div>
</body>
</html>
```